Redesign of an existing webpage

We've just redesigned our logo on a new website design to reflect the new logo. That wants to change the color and graphical appearance of our website. There are no restrictions on what should be changed. IT should display our portfolio and pricing and explain our product. Please provide stock photos if needed. The site structure should not be changed. So we want the pages which are currently there. We need the following pages: Main page (Home page) Detail page (currently used at AGB and questions) Imprint (including the map) existing webpage: www.brightdune.de
Updates

I've got a request from one of the designers-

Target Market(s)

We are offering IT services to small companies. The do not need own IT equipment or PC Specialists if if our service.

Industry/Entity Type

It Service

Coding

Coded - Design and coding required

Number of Pages Required

3 page

Font styles to use
Other font styles liked:
• Relaway

Colors

Designer to choose colors to be used in the design.

Requirements
Must have
• our login mask at https://desktop.brightdune.com needs a rebranding too

```html
<!DOCTYPE html>
<html lang="en">
<head>
<meta charset="utf-8">
<title>BrightDune – IT that just works</title>
<link href="https://fonts.googleapis.com/css2?family=Raleway:wght@500;600;700;800&family=Lato:wght@400;700&display=swap" rel="stylesheet">
<style>
:root{
  --blue:#0b5cbf;
  --blue-deep:#0a4aa8;
  --blue-title:#1757b3;
  --blue-soft:#2f7be0;
  --ink:#1b1b1b;
  --text:#4a4a4a;
  --muted:#6b6b6b;
  --green:#4cb81c;
  --band:#eef2f8;
  --white:#ffffff;
  --black:#000000;
}
*{box-sizing:border-box;margin:0;padding:0}
html,body{width:1200px;height:3302px;overflow:hidden;background:var(--white)}
body{position:relative;font-family:"Lato",sans-serif;color:var(--text)}
.abs{position:absolute}
h1,h2,h3,h4,.nav a,.btn{font-family:"Raleway",sans-serif}

/* hero */
.hero-bg{left:0;top:0}
.brand{left:97px;top:28px;font-family:"Raleway",sans-serif;font-weight:700;font-size:36px;letter-spacing:5px;color:var(--white)}
.nav{top:40px;left:490px;display:flex;gap:30px}
.nav a{color:var(--white);text-decoration:none;font-weight:700;font-size:15px;text-transform:uppercase}
.nav-cta{left:955px;top:33px;width:144px;height:38px;border:2px solid var(--white);border-radius:19px;color:var(--white);font-family:"Raleway",sans-serif;font-weight:700;font-size:13px;display:flex;align-items:center;justify-content:center}
.hero-title{left:158px;top:230px;color:var(--white);font-size:39px;font-weight:800}
.hero-text{left:158px;top:290px;width:500px;color:var(--white);font-size:21px;line-height:27px;font-weight:400;font-family:"Raleway",sans-serif}
.hero-btn{left:156px;top:394px;width:194px;height:57px;border:2px solid var(--white);border-radius:29px;color:var(--white);font-weight:700;font-size:18px;display:flex;align-items:center;justify-content:center}
.arrow{top:310px}

/* feature cards */
.card{width:260px;height:337px;top:617px;background:var(--white);border-radius:6px;box-shadow:0 4px 18px rgba(0,0,0,.12);text-align:center}
.card .icon{position:absolute;left:83px;top:15px;width:94px;height:94px;border-radius:50%;background:var(--white);box-shadow:0 3px 10px rgba(0,0,0,.18);display:flex;align-items:center;justify-content:center}
.card h3{position:absolute;top:129px;width:100%;color:var(--blue-title);font-size:18px;font-weight:700}
.card p{position:absolute;top:163px;left:30px;right:30px;font-size:13px;line-height:20.5px;color:var(--text)}
.pill{background:var(--blue);color:var(--white);border-radius:20px;font-weight:700;display:flex;align-items:center;justify-content:center;box-shadow:0 3px 6px rgba(0,0,0,.2)}
.card .pill{position:absolute;left:58px;top:259px;width:145px;height:35px;font-size:12.5px}

/* benefits */
.section-title{width:1200px;text-align:center;color:var(--ink);font-size:29px;font-weight:700}
.benefit-icon{width:84px;height:84px;border-radius:14px;background:var(--white);box-shadow:0 0 10px rgba(0,0,0,.12);transform:rotate(45deg)}
.benefit-glyph{width:60px;height:60px}
.benefit h4{color:var(--blue-title);font-size:20px;font-weight:700;line-height:23px}
.benefit p{margin-top:4px;font-size:14px;line-height:19px;color:var(--muted)}
.view-btn{left:495px;top:1459px;width:204px;height:47px;font-size:18px;border-radius:24px}

/* select service */
.service-title{left:164px;top:1642px;color:var(--ink);font-size:28px;font-weight:700}
.service-text{left:162px;top:1700px;width:280px;font-size:16px;line-height:21px;color:var(--muted)}
.plan{width:253px;height:336px;top:1597px;background:var(--white);box-shadow:0 4px 16px rgba(0,0,0,.1);text-align:center}
.plan-photo{position:absolute;left:0;top:0;width:253px;height:121px;background:linear-gradient(135deg,#7a7f86,#3d4249 60%,#5a5e64)}
.plan-bump{position:absolute;left:86px;top:92px;width:81px;height:60px;border-radius:50%;background:var(--white)}
.plan h4{position:absolute;top:45px;width:100%;color:var(--white);font-size:19px;font-weight:600}
.plan .glyph{position:absolute;left:106px;top:98px}
.plan .price{position:absolute;top:160px;width:100%;color:var(--ink);font-family:"Raleway",sans-serif;font-size:19px;font-weight:700}
.plan ul{position:absolute;top:197px;left:44px;list-style:none;text-align:left}
.plan li{font-size:11.5px;line-height:25.5px;color:var(--ink);display:flex;align-items:center;gap:5px}
.plan li svg{flex:none}
.plan .go{position:absolute;left:51px;top:313px;width:151px;height:35px;background:var(--green);color:var(--white);border-radius:18px;font-weight:700;font-size:13px;display:flex;align-items:center;justify-content:center;font-family:"Raleway",sans-serif}

/* about */
.about-art{left:135px;top:2100px;width:470px;height:335px;border-radius:46% 54% 40% 60% / 38% 40% 60% 62%;background:radial-gradient(ellipse at 55% 45%,#dfe9f5,#e8eef7 60%,#f2f5fa)}
.about-title{left:642px;top:2155px;color:var(--blue-title);font-size:27px;font-weight:700}
.about-text{left:640px;top:2205px;width:420px;font-size:15px;line-height:20.5px;color:var(--muted)}
.about-text p+p{margin-top:21px}
.about-btn{left:638px;top:2374px;width:190px;height:45px;font-size:17px;border-radius:23px}

/* founders */
.founders-title{top:2577px;color:var(--white)}
.portrait{width:198px;height:198px;border-radius:50%;background:radial-gradient(circle at 50% 40%,#c9a58c,#8a7a70 55%,#d4d4d4 80%)}
.founder{color:var(--white)}
.founder h4{font-size:21px;font-weight:700}
.founder .role{font-family:"Raleway",sans-serif;font-weight:700;font-size:15px;margin-top:8px}
.founder p{font-size:12.5px;line-height:19.5px;margin-top:14px;width:220px}
.founder .outline{margin-top:14px;width:121px;height:34px;border:1.5px solid var(--white);border-radius:17px;display:flex;align-items:center;justify-content:center;font-family:"Raleway",sans-serif;font-weight:700;font-size:11px}

/* footer */
.foot-brand{top:3070px;width:1200px;text-align:center;font-family:"Raleway",sans-serif;font-weight:700;font-size:36px;letter-spacing:5px;color:var(--blue-soft)}
.foot-nav{top:3145px;width:1200px;display:flex;justify-content:center;gap:33px}
.foot-nav a{color:var(--white);text-decoration:none;font-family:"Raleway",sans-serif;font-weight:700;font-size:17px}
.copy{top:3180px;width:1200px;text-align:center;color:#cfcfcf;font-family:"Raleway",sans-serif;font-size:16px}
.social{top:3223px;left:502px;display:flex;gap:12px}
.social span{width:38px;height:38px;border-radius:50%;background:var(--blue)}
</style>
</head>
<body>

<!-- hero -->
<svg class="abs hero-bg" width="1200" height="760" viewBox="0 0 1200 760" role="img" aria-label="Photo of a smiling team working at office workstations, tinted blue">
  <defs>
    <linearGradient id="heroFill" x1="0" y1="0" x2="1" y2="1">
      <stop offset="0" stop-color="#2a6ed1"/>
      <stop offset=".45" stop-color="#3a7fdb"/>
      <stop offset="1" stop-color="#0c4fb0"/>
    </linearGradient>
  </defs>
  <path d="M0 0H1200V526C1080 640 880 720 640 737C420 748 200 700 0 647Z" fill="url(#heroFill)"/>
  <path d="M0 560C250 660 480 720 700 705C900 690 1080 620 1200 526V760H0Z" fill="#0b57bd" opacity=".0"/>
</svg>

<div class="abs brand">BRIGHTDUNE</div>
<nav class="abs nav">
  <a href="#">Home</a><a href="#">That's how it's done</a><a href="#">Prices</a><a href="#">About us</a>
</nav>
<div class="abs nav-cta">GET STARTED</div>

<h1 class="abs hero-title">IT THAT JUST WORKS</h1>
<p class="abs hero-text">In large companies, IT departments ensure a functioning IT. Central servers are used, which are accessed from the individual workstations</p>
<div class="abs btn hero-btn">LEARN MORE</div>

<svg class="abs arrow" style="left:70px" width="28" height="56" viewBox="0 0 28 56"><path d="M26 2L2 28L26 54" fill="none" stroke="#fff" stroke-width="2.5"/></svg>
<svg class="abs arrow" style="left:1092px" width="28" height="56" viewBox="0 0 28 56"><path d="M2 2L26 28L2 54" fill="none" stroke="#fff" stroke-width="2.5"/></svg>

<!-- feature cards -->
<div class="abs card" style="left:162px">
  <div class="icon"><svg width="60" height="60" viewBox="0 0 60 60" fill="none" stroke="#0b5cbf" stroke-width="2.5"><rect x="13" y="13" width="34" height="34" rx="3" transform="rotate(45 30 30)"/><rect x="18" y="18" width="24" height="24" rx="2" transform="rotate(45 30 30)"/><line x1="30" y1="21" x2="30" y2="33"/><circle cx="30" cy="38.5" r="1.5" fill="#0b5cbf"/></svg></div>
  <h3>THE PROBLEM</h3>
  <p>The basis of the IT problems that unnecessarily complicate your daily business is - in addition to the human factor</p>
  <div class="pill btn">LEARN MORE</div>
</div>
<div class="abs card" style="left:467px">
  <div class="icon"><svg width="60" height="60" viewBox="0 0 60 60" fill="none" stroke="#0b5cbf" stroke-width="2.5"><circle cx="30" cy="30" r="22"/><circle cx="30" cy="30" r="14"/><circle cx="30" cy="30" r="7"/><path d="M30 8v6M30 46v6M8 30h6M46 30h6"/></svg></div>
  <h3>OUR SOLUTION</h3>
  <p>BrightDune provides you with a solution that ensures the daily backup of your data and the monitoring of the operational</p>
  <div class="pill btn">LEARN MORE</div>
</div>
<div class="abs card" style="left:772px">
  <div class="icon"><svg width="60" height="60" viewBox="0 0 60 60" fill="none" stroke="#0b5cbf" stroke-width="2.5"><path d="M30 8L48 15V30C48 41 40 49 30 53C20 49 12 41 12 30V15Z"/><path d="M30 14L42 19V30C42 38 37 44 30 47C23 44 18 38 18 30V19Z"/><circle cx="30" cy="30" r="6"/><path d="M27 30l2 2 4-4"/></svg></div>
  <h3>YOUR SAFETY</h3>
  <p>If you're wondering how secure our solution is, the answer is simple: very safe. We work with Nordvault, one of Germany's</p>
  <div class="pill btn">LEARN MORE</div>
</div>

<!-- benefits -->
<h2 class="abs section-title" style="top:1040px">YOUR BENEFITS AT A GLANCE</h2>

<div class="abs benefit-icon" style="left:149px;top:1152px"></div>
<svg class="abs benefit-glyph" style="left:161px;top:1164px" viewBox="0 0 60 60" fill="none" stroke="#0b5cbf" stroke-width="2.2"><path d="M20 52V42C12 38 10 30 12 22C15 12 26 8 35 11C44 14 48 22 46 30L50 38H45V45H38V52"/><circle cx="32" cy="24" r="6"/><path d="M32 14v4M32 30v4M22 24h4M38 24h4"/></svg>
<div class="abs benefit" style="left:263px;top:1137px;width:290px">
  <h4>EXPRESS<br>SUPPRESSION</h4>
  <p>Mondays to Fridays the troubleshooting is done in a maximum of 8 hours by the BrightDune Support</p>
</div>

<div class="abs benefit-icon" style="left:620px;top:1150px"></div>
<svg class="abs benefit-glyph" style="left:632px;top:1162px" viewBox="0 0 60 60" fill="none" stroke="#0b5cbf" stroke-width="2.4"><path d="M10 40A20 20 0 1 1 50 40"/><path d="M8 40H52"/><path d="M30 38L22 26"/><path d="M14 28l3 2M46 28l-3 2M30 16v4M20 19l2 3M40 19l-2 3"/></svg>
<div class="abs benefit" style="left:735px;top:1137px;width:310px">
  <h4>FAST<br>PROGRAMS</h4>
  <p>Our technology brings the maximum speed out of your existing applications</p>
</div>

<div class="abs benefit-icon" style="left:153px;top:1317px"></div>
<svg class="abs benefit-glyph" style="left:165px;top:1329px" viewBox="0 0 60 60" fill="none" stroke="#0b5cbf" stroke-width="2.4"><ellipse cx="30" cy="14" rx="20" ry="6"/><path d="M10 14V46C10 49 19 52 30 52S50 49 50 46V14"/><path d="M10 25C10 28 19 31 30 31S50 28 50 25M10 36C10 39 19 42 30 42S50 39 50 36"/></svg>
<div class="abs benefit" style="left:265px;top:1308px;width:260px">
  <h4>DATA BACKUP</h4>
  <p>Daily data backup and thus protection against data loss - controlled by us and recoverable at any time</p>
</div>

<div class="abs benefit-icon" style="left:623px;top:1315px"></div>
<svg class="abs benefit-glyph" style="left:635px;top:1327px" viewBox="0 0 60 60" fill="none" stroke="#0b5cbf" stroke-width="2.2"><rect x="6" y="30" width="8" height="18"/><path d="M14 34H28L36 38H28M14 46L26 50L52 38C52 34 48 33 44 35L36 38"/><path d="M38 10A8 8 0 1 0 38 24M28 15H38M28 19H38"/></svg>
<div class="abs benefit" style="left:738px;top:1308px;width:300px">
  <h4>PREDICTABLE COSTS</h4>
  <p>Linear monthly cost distribution. Additional costs due to defects, extensions or expensive on-site operations are not incurred</p>
</div>

<!-- select service band -->
<svg class="abs" style="left:0;top:1490px" width="1200" height="580" viewBox="0 0 1200 580" role="img" aria-label="Faded photo of an office desk with a laptop in light grey-blue tones">
  <defs>
    <linearGradient id="bandFill" x1="0" y1="0" x2="0" y2="1">
      <stop offset="0" stop-color="#f7f9fc"/>
      <stop offset=".3" stop-color="#e9eef6"/>
      <stop offset=".8" stop-color="#eef2f8"/>
      <stop offset="1" stop-color="#fafbfd"/>
    </linearGradient>
  </defs>
  <path d="M0 0C300 20 900 40 1200 30V520C900 580 300 580 0 520Z" fill="url(#bandFill)"/>
</svg>
<div class="abs view-btn pill btn">VIEW MORE</div>

<h2 class="abs service-title">SELECT SERVICE</h2>
<div class="abs service-text">
  <p>Choose your service. BrightDune provides a complete workstation in the Thin Client model All you need is a monitor to get started.</p>
  <p style="margin-top:21px">Both services can be encrypted using an existing PC, laptop or tablet from any location.</p>
</div>

<div class="abs plan" style="left:478px">
  <div class="plan-photo" role="img" aria-label="Photo of business people meeting at a table"></div>
  <div class="plan-bump"></div>
  <h4>THE CLIENT</h4>
  <svg class="glyph" width="42" height="42" viewBox="0 0 42 42" fill="none" stroke="#0b5cbf" stroke-width="1.8"><circle cx="11" cy="9" r="4"/><circle cx="21" cy="9" r="4"/><circle cx="31" cy="9" r="4"/><path d="M4 22C4 16 18 16 18 22M14 22C14 16 28 16 28 22M24 22C24 16 38 16 38 22"/><path d="M4 34L12 28H24L20 32H28L36 26L38 28L30 38H12L8 38Z"/></svg>
  <div class="price">FROM 99 €</div>
  <ul>
    <li><svg width="12" height="12" viewBox="0 0 12 12"><circle cx="6" cy="6" r="6" fill="#0b5cbf"/><path d="M3 6l2 2 4-4" stroke="#fff" stroke-width="1.6" fill="none"/></svg>up to 5 users 115 € / month</li>
    <li><svg width="12" height="12" viewBox="0 0 12 12"><circle cx="6" cy="6" r="6" fill="#0b5cbf"/><path d="M3 6l2 2 4-4" stroke="#fff" stroke-width="1.6" fill="none"/></svg>Minimum term 12 months</li>
    <li><svg width="12" height="12" viewBox="0 0 12 12"><circle cx="6" cy="6" r="6" fill="#0b5cbf"/><path d="M3 6l2 2 4-4" stroke="#fff" stroke-width="1.6" fill="none"/></svg>Thinclient per user included</li>
    <li><svg width="12" height="12" viewBox="0 0 12 12"><circle cx="6" cy="6" r="6" fill="#0b5cbf"/><path d="M3 6l2 2 4-4" stroke="#fff" stroke-width="1.6" fill="none"/></svg>Max. 8 hours reaction time</li>
  </ul>
  <div class="go">GET STARTED</div>
</div>

<div class="abs plan" style="left:770px">
  <div class="plan-photo" role="img" aria-label="Photo of a team working together at laptops"></div>
  <div class="plan-bump"></div>
  <h4>BRING YOUR OWN</h4>
  <svg class="glyph" width="42" height="42" viewBox="0 0 42 42" fill="none" stroke="#0b5cbf" stroke-width="2"><circle cx="21" cy="12" r="7"/><path d="M8 38C8 28 14 23 21 23S34 28 34 38"/></svg>
  <div class="price">FROM 75 €</div>
  <ul>
    <li><svg width="12" height="12" viewBox="0 0 12 12"><circle cx="6" cy="6" r="6" fill="#0b5cbf"/><path d="M3 6l2 2 4-4" stroke="#fff" stroke-width="1.6" fill="none"/></svg>up to 5 users 115 € / month</li>
    <li><svg width="12" height="12" viewBox="0 0 12 12"><circle cx="6" cy="6" r="6" fill="#0b5cbf"/><path d="M3 6l2 2 4-4" stroke="#fff" stroke-width="1.6" fill="none"/></svg>Minimum term 12 months</li>
    <li><svg width="12" height="12" viewBox="0 0 12 12"><circle cx="6" cy="6" r="6" fill="#0b5cbf"/><path d="M3 6l2 2 4-4" stroke="#fff" stroke-width="1.6" fill="none"/></svg>Thinclient per user included</li>
    <li><svg width="12" height="12" viewBox="0 0 12 12"><circle cx="6" cy="6" r="6" fill="#0b5cbf"/><path d="M3 6l2 2 4-4" stroke="#fff" stroke-width="1.6" fill="none"/></svg>Max. 8 hours reaction time</li>
  </ul>
  <div class="go">GET STARTED</div>
</div>

<!-- about -->
<div class="abs about-art" role="img" aria-label="Illustration of a woman sitting cross-legged working on a laptop in front of a bookshelf, in soft blue, grey and coral tones"></div>
<h2 class="abs about-title">SIMPLE, RELIABLE AND CHEAP</h2>
<div class="abs about-text">
  <p>Big companies have been working this way for years, cutting costs and improving stability. Now BrightDune offers the solution for even the smallest businesses.</p>
  <p>We store your data permanently in a safe place. Necessary security measures are taken, your data is backed up and you focus on your daily business.</p>
</div>
<div class="abs about-btn pill btn">LEARN MORE</div>

<!-- founders & footer backgrounds -->
<div class="abs" style="left:0;top:2960px;width:1200px;height:342px;background:var(--black)"></div>
<svg class="abs" style="left:0;top:2510px" width="1200" height="520" viewBox="0 0 1200 520">
  <path d="M0 47C300 0 900 0 1200 47V448C900 530 300 530 0 452Z" fill="#0b57bd"/>
</svg>

<h2 class="abs section-title founders-title">THE FOUNDERS</h2>

<div class="abs portrait" style="left:164px;top:2653px" role="img" aria-label="Portrait photo of the first co-founder"></div>
<div class="abs founder" style="left:381px;top:2684px">
  <h4>LUKAS BRENNING</h4>
  <div class="role">FOUNDER AND CEO</div>
  <p>Lukas is 46 years old, married and has two children. He has been working in IT for 19 years now and, as a trained merchant, has made a difference. In addition</p>
  <div class="outline">LEARN MORE</div>
</div>

<div class="abs portrait" style="left:628px;top:2657px" role="img" aria-label="Portrait photo of the second co-founder"></div>
<div class="abs founder" style="left:846px;top:2677px">
  <h4>JONAS WEIDLICH</h4>
  <div class="role">FOUNDER AND CEO</div>
  <p>Jonas is 34 years old and single. He has been working in the computer industry for more than 15 years since his training as a computer specialist and his degree</p>
  <div class="outline">LEARN MORE</div>
</div>

<!-- footer -->
<div class="abs foot-brand">BRIGHTDUNE</div>
<nav class="abs foot-nav">
  <a href="#">HOME</a><a href="#">THAT'S HOW IT'S DONE</a><a href="#">PRICES</a><a href="#">ABOUT US</a><a href="#">CONTACT US</a>
</nav>
<div class="abs copy">© 2019 Company Name &nbsp;All right reserved</div>
<div class="abs social"><span></span><span></span><span></span><span></span></div>

</body>
</html>
```